Business Card Design Project - Sports Brand

Brisk is a e-commerce fitness wear brand for ladies who are into gym, pole and swim.

Card should not be overly cluttered and should include the following:

1. logo
2. Name of the company (Use "Brisk Loom Pte Ltd" for now)
3. Address of company (Use a mock address)
4. Representative's name and contact info etc. (use a mock name and contact info)
5. website address

Target Market(s)

Women who are into pole , gym, and swim.

Women who shop online

Industry/Entity Type

E-Commerce

Colors

Designer to choose colors to be used in the design.

Requirements
Nice to have
• feminine sublimation of colours

Need not be printed on traditional paper. We would like the design to be revolutionary and interesting to the eye :)
Should not have
• the design should not be traditional looking. Do not include illustrations of Bikinis, yoga poses etc. in the card.

```html
<!DOCTYPE html>
<html lang="en">
<head>
<meta charset="utf-8">
<title>Brisk Loom – Business Cards</title>
<link href="https://fonts.googleapis.com/css2?family=Exo+2:wght@400;600&family=PT+Serif&family=Yesteryear&display=swap" rel="stylesheet">
<style>
  :root {
    --stage: #ece8e4;
    --card: #ffffff;
    --berry: #b8323f;
    --berry-soft: #c9444f;
    --ink: #3a3a3a;
    --splash-pink: #e56aa6;
    --splash-coral: #f08a5d;
    --splash-rose: #f4b3cf;
  }
  * { box-sizing: border-box; margin: 0; padding: 0; }
  html, body {
    width: 1200px; height: 900px; overflow: hidden;
    background: var(--stage);
    font-family: "Exo 2", sans-serif;
  }
  .stage { position: relative; width: 1200px; height: 900px; }

  .card {
    position: absolute;
    width: 560px; height: 320px;
    background: var(--card);
    box-shadow: 0 10px 30px rgba(0,0,0,0.12);
    overflow: hidden;
  }
  .card--front { left: 70px; top: 110px; }
  .card--back { left: 570px; top: 470px; }

  .card__stripes { position: absolute; top: 0; right: 26px; height: 100%; width: 40px; }

  /* Front */
  .splash {
    position: absolute; left: 40px; top: 60px;
    width: 230px; height: 210px;
    border-radius: 48% 52% 46% 54% / 52% 46% 54% 48%;
    background: radial-gradient(circle at 70% 70%, var(--splash-coral) 0%, var(--splash-pink) 55%, var(--splash-rose) 100%);
    opacity: 0.9;
  }
  .brand-name {
    position: absolute; left: 200px; top: 108px;
    font-family: "Exo 2", sans-serif; font-weight: 600;
    font-size: 68px; line-height: 1; color: var(--berry);
  }
  .brand-tagline {
    position: absolute; left: 230px; top: 188px;
    font-family: "PT Serif", serif; font-size: 22px; color: var(--ink);
  }

  /* Back */
  .company {
    position: absolute; right: 96px; top: 44px;
    font-family: "Yesteryear", cursive; font-size: 30px; color: var(--berry);
  }
  .contact {
    position: absolute; right: 96px; top: 96px;
    text-align: right; color: var(--berry-soft);
    font-size: 15px; line-height: 1.3;
  }
  .contact__name { font-size: 20px; }
  .contact__role { font-size: 12px; color: var(--ink); margin-bottom: 14px; }
  .contact__row { display: flex; justify-content: flex-end; align-items: center; gap: 8px; }
  .contact__row svg { width: 13px; height: 13px; fill: var(--berry-soft); }
  .contact__address { margin-top: 14px; }
  .brand-mark-large {
    position: absolute; left: 36px; bottom: 30px;
    font-family: "Exo 2", sans-serif; font-weight: 600;
    font-size: 110px; line-height: 1; color: var(--berry);
  }
</style>
</head>
<body>
<main class="stage">

  <section class="card card--front" aria-label="Business card front">
    <div class="splash" role="img" aria-label="Soft pink and coral watercolour splash"></div>
    <div class="brand-name">Brisk</div>
    <div class="brand-tagline">Yoga•Swim•Pole</div>
    <svg class="card__stripes" viewBox="0 0 40 320" preserveAspectRatio="none" aria-hidden="true">
      <g stroke="var(--berry)" stroke-width="3">
        <line x1="6" y1="0" x2="6" y2="320"/>
        <line x1="18" y1="0" x2="18" y2="320"/>
        <line x1="30" y1="0" x2="30" y2="320"/>
      </g>
    </svg>
  </section>

  <section class="card card--back" aria-label="Business card back">
    <div class="company">Brisk Loom Pte Ltd</div>
    <div class="contact">
      <div class="contact__name">Mara Quinn</div>
      <div class="contact__role">Manager</div>
      <div class="contact__row">+123 555 0142
        <svg viewBox="0 0 16 16" aria-hidden="true"><path d="M3 1l3 1 1 3-2 1.5a9 9 0 0 0 4.5 4.5L11 9l3 1 1 3-2 2C7 15 1 9 1 3z"/></svg>
      </div>
      <div class="contact__row">mara@mail.com
        <svg viewBox="0 0 16 16" aria-hidden="true"><path d="M1 3h14v10H1zM2 4l6 5 6-5v1L8 10 2 5z"/></svg>
      </div>
      <div class="contact__row">www.briskloom.com
        <svg viewBox="0 0 16 16" aria-hidden="true"><path d="M8 1a5 5 0 0 1 4 8l-4 6-4-6a5 5 0 0 1 4-8zm0 3a2 2 0 1 0 0 4 2 2 0 0 0 0-4z"/></svg>
      </div>
      <div class="contact__row contact__address">Building No.1, Street
        <svg viewBox="0 0 16 16" aria-hidden="true"><path d="M8 1l7 7h-2v7H9v-4H7v4H3V8H1z"/></svg>
      </div>
      <div class="contact__row">City Zipcode<span style="width:13px"></span></div>
    </div>
    <div class="brand-mark-large">Brisk</div>
    <svg class="card__stripes" viewBox="0 0 40 320" preserveAspectRatio="none" aria-hidden="true">
      <g stroke="var(--berry)" stroke-width="3">
        <line x1="6" y1="0" x2="6" y2="320"/>
        <line x1="18" y1="0" x2="18" y2="320"/>
        <line x1="30" y1="0" x2="30" y2="320"/>
      </g>
    </svg>
  </section>

</main>
</body>
</html>
```